Bright Path Flyer Design for Virtual Online Clinic. -5.5 x 8.5 inches (half sheet)

We need a clean, modern flyer design for Bright Path, a new virtual walk-in clinic based in British Columbia. The flyer will be used in libraries, pharmacies, and community centers to help residents easily access primary care through their Bright Path NFC access card.
The flyer will ask a question : NEED A DOCTOR? This should be large and attention grabbing.
The design should clearly feature a Bright Path card image (the access card) as the centerpiece and visually show how patients can use it to book appointments. The tone should feel trustworthy, healthcare-oriented, and community-friendly — clean fonts, clear spacing, and strong readability from a distance.

Side One: This card has the NFC Access Card.
NEED A DOCTOR? (Large Font, Attention Grabbing)
How to Book an Appointment using your Bright Path Card
Step 1: Tap Your Card on Your Phone
Hold your card near the back of your phone.
It will activate automatically — no app needed.
The Bright Path scheduler will open.
Step 2: Schedule Your Appointment
Select your clinical concern.
Choose your time window.
Register (only once).
Confirm your appointment.
Step 3: Relax, we’ll take care of the rest
A doctor will call during your scheduled time.
Once booked, you’ll be able to call our office.
No emails, no texts — just a real person.
It’s that simple.
Side Two:
About Bright Path
Created by Dr. Marcus Ferrigan
Bright Path was founded to make healthcare simple and convenient. Prescription renewals. Common infections. Medical notes. And so much more.
Our doctors can address 120+ health concerns virtually — providing quality care without the waiting room. No waiting rooms. Just real doctors providing real care.
Why Patients Choose Bright Path
Easy access – book and be seen from anywhere in BC.
Effortless booking – tap your Bright Path Card to begin.
Trusted physicians – every visit is with a licensed BC family doctor.
How It Works
Book your visit — choose a time window that fits your day.
Join the queue — you’ll be called when it’s your turn.
Speak directly with your doctor — simple, secure, and stress-free.
Convenient Care for Common Concerns

Additional Details.
Please find the domain to be launched soon. I've attached the NFC card file for review, it is 85.5 mm x 54 mm. The card will be glued to the flyer.
I've attached examples of flyers but they are not the look I am seeking and I am looking for creative solutions.
Thank you!
http://brightpath-example.test/

Adult Patients in British Columbia

Healthcare

• Looking for clean lines, uniform appearance, and high legibility i.e poppins

0054AA
0677BA
7BADD7
CADEEF
E8F1F8

• Need A Doctor?
• Elegant style, not too busy, clear layout.
• Clutter, look cheap - review examples.

```html
<!DOCTYPE html>
<html lang="en">
<head>
<meta charset="utf-8">
<title>Bright Path Flyer Design – Virtual Online Clinic</title>
<link href="https://fonts.googleapis.com/css2?family=Poppins:ital,wght@0,300;0,400;0,500;0,600;0,700;1,300;1,400;1,600&display=swap" rel="stylesheet">
<style>
  :root {
    --teal: #245b69;
    --teal-text: #2f6676;
    --sky: #cadeef;
    --sky-soft: #e8f1f8;
    --navy: #0b3f8a;
    --step-blue: #1b4f8e;
    --gold: #8a6f36;
    --body: #4c6670;
    --white: #ffffff;
    --board-text: #5b5b5b;
  }
  * { box-sizing: border-box; margin: 0; padding: 0; }
  html, body { width: 1200px; height: 956px; overflow: hidden; background: var(--white); }
  body { font-family: "Poppins", sans-serif; }

  .board { position: relative; width: 1135px; height: 904px; transform: scale(1.0573); transform-origin: 0 0; }

  .board-title { position: absolute; left: 60px; top: 30px; text-align: right; width: 289px; color: var(--board-text); font-weight: 300; line-height: 1.08; }
  .board-title .line-1 { font-size: 22px; }
  .board-title .line-1 em { font-style: italic; }
  .board-title .line-2 { font-size: 17px; }
  .board-divider { position: absolute; left: 356px; top: 30px; width: 1px; height: 48px; background: var(--navy); }
  .board-size { position: absolute; left: 370px; top: 42px; font-size: 21px; font-weight: 300; color: var(--board-text); }

  .flyer { position: absolute; top: 152px; width: 397px; height: 612px; background: var(--white); overflow: hidden; box-shadow: 2px 4px 8px rgba(0,0,0,.28); }
  .flyer--front { left: 135px; }
  .flyer--back { left: 613px; }
  .flyer-shapes { position: absolute; inset: 0; width: 397px; height: 612px; }
  .abs { position: absolute; }

  /* Front */
  .headline { left: 168px; top: 62px; color: var(--white); font-weight: 600; font-size: 43px; line-height: 1; letter-spacing: -.3px; }
  .card-slot { left: 137px; top: 163px; width: 243px; height: 154px; border: 1.5px solid var(--sky); border-radius: 16px; background: var(--white); }
  .book-badge { left: 17px; top: 212px; width: 114px; height: 114px; border-radius: 50%; background: var(--navy); color: var(--white); text-align: center; font-size: 11px; line-height: 1.17; display: flex; flex-direction: column; justify-content: center; }
  .book-badge strong { font-weight: 600; }
  .book-badge .brand { font-weight: 700; font-style: italic; }

  .step { left: 109px; width: 243px; font-size: 8.2px; line-height: 1.47; color: var(--body); text-align: justify; }
  .step-title { font-size: 10.2px; color: var(--step-blue); text-align: left; margin-bottom: 1px; font-weight: 400; }
  .step-title b { color: var(--gold); font-weight: 600; }
  .step ul { list-style: none; text-align: left; }
  .step-icon { left: 49px; width: 48px; height: 48px; border-radius: 50%; background: var(--sky); display: flex; align-items: center; justify-content: center; }

  .site-url { left: 49px; top: 572px; font-size: 10px; color: var(--teal); }
  .front-brand { left: 278px; top: 552px; color: var(--white); font-size: 13px; font-weight: 500; }
  .front-tagline { left: 278px; top: 577px; color: var(--white); font-size: 10px; font-weight: 500; }

  /* Back */
  .about-title { left: 37px; top: 38px; color: var(--white); font-size: 11.5px; font-weight: 400; }
  .about-title em { font-style: italic; }
  .about-copy { left: 37px; color: var(--teal-text); font-size: 7.9px; line-height: 1.52; text-align: justify; }
  .why-title { left: 37px; top: 234px; color: var(--white); font-size: 10.6px; line-height: 1.35; font-weight: 400; }
  .why-item { left: 37px; color: var(--white); font-size: 8.2px; line-height: 1.75; }
  .why-item b { font-weight: 500; }
  .why-item em { display: block; padding-left: 5px; font-weight: 300; }
  .how-title { left: 51px; top: 448px; color: var(--gold); font-size: 11px; font-weight: 600; }
  .how-list { left: 51px; top: 468px; list-style: none; font-size: 8.2px; line-height: 1.85; color: var(--body); }
  .how-list b { color: var(--step-blue); font-weight: 500; }
  .back-brand { left: 55px; top: 550px; color: var(--teal); font-size: 13px; font-weight: 500; }
  .back-tagline { left: 142px; top: 552px; color: var(--teal); font-size: 10px; font-style: italic; font-weight: 400; }
</style>
</head>
<body>
<div class="board">
  <div class="board-title">
    <div class="line-1">Bright Path <em>Flyer Design</em></div>
    <div class="line-2">for Virtual Online Clinic</div>
  </div>
  <div class="board-divider"></div>
  <div class="board-size">5.5 x 8.5 inches</div>

  <!-- Side one -->
  <section class="flyer flyer--front">
    <svg class="flyer-shapes" viewBox="0 0 397 612">
      <defs>
        <linearGradient id="heroFill" x1="0" y1="0" x2="1" y2="0.3">
          <stop offset="0" stop-color="#c7d8df"/>
          <stop offset=".45" stop-color="#7fb6c8"/>
          <stop offset="1" stop-color="#245b69"/>
        </linearGradient>
      </defs>
      <path d="M0 240 C80 236 150 232 220 220 C290 208 350 196 397 186 V210 C330 230 250 246 180 252 C110 258 50 256 0 254 Z" fill="var(--sky)"/>
      <path d="M0 0 H397 V186 C350 196 290 208 220 220 C150 232 80 236 0 240 Z" fill="var(--teal)"/>
      <rect x="0" y="0" width="200" height="236" fill="url(#heroFill)" role="img" aria-label="Photo of a smiling woman using her phone, with floating healthcare icons"/>
      <path d="M0 555 C60 540 130 542 210 565 L210 612 H0 Z" fill="var(--sky)"/>
      <path d="M140 612 C210 600 240 555 310 537 C345 528 372 528 397 530 V612 Z" fill="var(--teal)"/>
    </svg>

    <h1 class="abs headline">Need a<br>DOCTOR?</h1>
    <div class="abs card-slot" aria-label="Access card placement"></div>

    <div class="abs book-badge">
      <strong>How to Book</strong>
      <span>an</span>
      <span>Appointment</span>
      <span>using your</span>
      <span class="brand">Bright Path</span>
      <span>Card</span>
    </div>

    <div class="abs step-icon" style="top:341px">
      <svg width="26" height="30" viewBox="0 0 26 30"><rect x="8" y="2" width="14" height="26" rx="2.5" fill="none" stroke="#5f8fc4" stroke-width="1.6"/><rect x="2" y="11" width="15" height="9" rx="1.5" fill="var(--navy)"/></svg>
    </div>
    <div class="abs step" style="top:339px">
      <p class="step-title"><b>Step 1</b>&nbsp; Tap Your Card on Your Phone</p>
      <p>Hold your card near the back of your phone. It will activate automatically / no app needed. The Bright Path scheduler will open.</p>
    </div>

    <div class="abs step-icon" style="top:411px">
      <svg width="26" height="30" viewBox="0 0 26 30"><rect x="4" y="5" width="18" height="23" rx="2" fill="none" stroke="#5f8fc4" stroke-width="1.6"/><rect x="9" y="2" width="8" height="5" rx="1" fill="#5f8fc4"/><path d="M8 17 L12 21 L19 12" fill="none" stroke="var(--navy)" stroke-width="2.2" stroke-linecap="round"/></svg>
    </div>
    <div class="abs step" style="top:398px">
      <p class="step-title"><b>Step 2</b> Schedule Your Appointment</p>
      <ul>
        <li>• Select your clinical concern.</li>
        <li>• Choose your time window.</li>
        <li>• Register (only once).</li>
        <li>• Confirm your appointment.</li>
      </ul>
    </div>

    <div class="abs step-icon" style="top:471px">
      <svg width="28" height="24" viewBox="0 0 28 24"><path d="M5 8 H19 V14 A7 7 0 0 1 5 14 Z" fill="var(--white)"/><path d="M19 10 H22 A2.5 2.5 0 0 1 22 15 H18" fill="none" stroke="var(--white)" stroke-width="1.6"/><rect x="2" y="20" width="22" height="2" rx="1" fill="var(--white)"/></svg>
    </div>
    <div class="abs step" style="top:467px">
      <p class="step-title"><b>Step 3</b> Relax</p>
      <p>We'll take care of the rest. A doctor will call during your scheduled time. Once booked, you'll be able to call our office. No emails, no texts — just a real person.</p>
    </div>

    <p class="abs site-url">www.brightpath-example.test</p>
    <p class="abs front-brand">Bright Path</p>
    <p class="abs front-tagline">It's that Simple.</p>
  </section>

  <!-- Side two -->
  <section class="flyer flyer--back">
    <svg class="flyer-shapes" viewBox="0 0 397 612">
      <defs>
        <linearGradient id="doctorFill" x1="0" y1="0" x2="1" y2="1">
          <stop offset="0" stop-color="#dfe9ef"/>
          <stop offset=".5" stop-color="#a9c6d6"/>
          <stop offset="1" stop-color="#6f93a6"/>
        </linearGradient>
      </defs>
      <path d="M300 0 H397 V30 C370 22 335 10 300 0 Z" fill="var(--sky)"/>
      <path d="M0 60 C60 62 130 72 200 55 C260 40 300 15 350 0 H397 V6 C340 22 300 48 230 68 C150 88 70 78 0 76 Z" fill="var(--sky)"/>
      <path d="M0 0 H350 C300 15 260 40 200 55 C130 72 60 62 0 60 Z" fill="var(--teal)"/>
      <path d="M0 405 C60 398 140 400 230 410 C300 418 360 420 397 418 V432 C330 436 240 428 150 420 C90 416 40 420 0 432 Z" fill="var(--sky)"/>
      <path d="M0 222 C70 205 150 208 230 230 L397 250 V415 C300 408 220 398 130 394 C70 392 30 398 0 408 Z" fill="var(--teal)"/>
      <ellipse cx="340" cy="270" rx="112" ry="150" fill="var(--teal)"/>
      <ellipse cx="342" cy="270" rx="102" ry="140" fill="url(#doctorFill)" role="img" aria-label="Photo of a smiling doctor with a stethoscope speaking with a patient"/>
    </svg>

    <h2 class="abs about-title">About <em>Bright Path</em></h2>
    <p class="abs about-copy" style="top:90px;width:250px">Created by Dr. Marcus Ferrigan, Bright Path was founded to make healthcare simple and convenient. Prescription renewals. Common infections. Medical notes. And so much more.</p>
    <p class="abs about-copy" style="top:147px;width:196px">Our doctors can address 120+ health concerns virtually — providing quality care without the waiting room. No waiting rooms. Just real doctors providing real care.</p>

    <h2 class="abs why-title">Why Patients<br>Choose Bright Path</h2>
    <p class="abs why-item" style="top:264px"><b>• Easy access</b><em>book and be seen from anywhere in BC.</em></p>
    <p class="abs why-item" style="top:309px"><b>• Effortless booking</b><em>Tap your Bright Path Card to begin.</em></p>
    <p class="abs why-item" style="top:354px"><b>• Trusted physicians</b><em>Every visit is with a licensed BC family doctor.</em></p>

    <h2 class="abs how-title">How It Works</h2>
    <ul class="abs how-list">
      <li><b>Book your visit</b> &gt; choose a time window that fits your day.</li>
      <li><b>Join the queue</b> &gt; you'll be called when it's your turn.</li>
      <li><b>Speak directly with your doctor</b> &gt; simple, secure, and stress-free.</li>
    </ul>

    <p class="abs back-brand">Bright Path</p>
    <p class="abs back-tagline">Convenient Care for Common Concerns</p>
  </section>
</div>
</body>
</html>
```